Surgical Procedure Room Letterhead

PLEASE DO NOT MAKE YOUR LETTERHEAD SIMILAR TO THE ONE I AM INCLUDING IN MY UPLOADS

Hello! I need my logo used to make a very clean, professional, simple letterhead that has all the pertinent information in it:
Location: 4829 NW 58th Lane, Suite 310
Coral Bend, FL 33468
Phone: 555-618-2450
Fax: 800-394-8261

Can you please put this all on a word document that is easily editable? I will include my practice letterhead as an example ONLY of how easy it should be to write below the letterhead. Please don't make this letterhead the same as the one I am including in this example. They are two separate businesses.

Target Market(s)

Insurance companies

Industry/Entity Type

medical

Requirements
Must have
• classiness, elegance, simplicity
Should not have
• Please don't make your letterhead the same as the one that I included in my uploads

```html
<!DOCTYPE html>
<html lang="en">
<head>
<meta charset="utf-8">
<title>Meridian Surgical Suites Letterhead</title>
<link rel="stylesheet" href="https://fonts.googleapis.com/css2?family=Lato:wght@400;700&family=Dancing+Script:wght@500&display=swap">
<style>
  :root {
    --backdrop: #e4e4e4;
    --paper: #ffffff;
    --navy: #16295a;
    --gold: #d4ae3b;
    --ink: #2b2b2b;
    --ink-soft: #3c3c3c;
  }
  * { box-sizing: border-box; margin: 0; padding: 0; }
  html, body {
    width: 1200px; height: 874px; overflow: hidden;
    background: var(--backdrop);
  }
  .letterhead {
    position: absolute; left: 310px; top: 27px;
    width: 580px; height: 820px;
    background: var(--paper);
    box-shadow: 0 2px 10px rgba(0,0,0,0.12);
    overflow: hidden;
    font-family: "Lato", sans-serif;
    color: var(--ink);
  }
  .brand {
    position: absolute; left: 58px; top: 52px;
    display: flex; align-items: center; gap: 10px;
  }
  .brand-dot {
    width: 30px; height: 30px; border-radius: 50%;
    background: var(--gold);
  }
  .brand-name {
    font-weight: 700; font-size: 19px; letter-spacing: 1.5px;
    text-transform: uppercase; color: var(--navy);
  }
  .letter {
    position: absolute; left: 78px; top: 150px; width: 440px;
    font-size: 8.6px; line-height: 1.32; color: var(--ink-soft);
  }
  .date { margin-bottom: 12px; }
  .recipient { margin-bottom: 10px; }
  .recipient-block { margin-bottom: 10px; }
  .salutation {
    font-size: 11px; font-weight: 700; color: var(--ink);
    margin-bottom: 10px;
  }
  .letter p.body { margin-bottom: 12px; padding-left: 22px; }
  .closing { padding-left: 60px; margin-top: 24px; }
  .signature {
    font-family: "Dancing Script", cursive; font-size: 34px;
    color: var(--ink); padding-left: 70px; margin-top: 4px;
  }
  .footer-wave { position: absolute; left: 0; top: 0; }
  .contact {
    position: absolute; left: 250px; top: 628px; width: 240px;
    font-style: normal; font-size: 8.6px; color: var(--ink); line-height: 1.6;
  }
  .contact-line { display: flex; align-items: center; justify-content: flex-end; gap: 5px; }
  .contact-line svg { flex: none; }
</style>
</head>
<body>
  <main class="letterhead">
    <header class="brand">
      <span class="brand-dot"></span>
      <span class="brand-name">Meridian Surgical Suites</span>
    </header>

    <section class="letter">
      <div class="date">Feb-03-2022</div>
      <div class="recipient">Mr. John Doe<br>President</div>
      <div class="recipient-block">Link Corporation<br>123 Street Name, Suite# 10<br>City, State, 120023</div>
      <div class="salutation">Dear Mr. John</div>
      <p class="body">Lorem ipsum dolor sit amet, consectetur adipisicing elit, sed do eiusmod tempor incididunt ut labore et dolore magna aliqua. Ut enim ad minim veniam, quis nostrud exercitation ullamco laboris nisi ut aliquip ex ea commodo consequat. Duis aute irure dolor in reprehenderit in voluptate velit esse cillum dolore eu fugiat nulla pariatur.</p>
      <p class="body">Lorem ipsum dolor sit amet, consectetur adipisicing elit, sed do eiusmod tempor incididunt ut labore et dolore magna aliqua. Ut enim ad minim veniam, quis nostrud exercitation ullamco laboris nisi ut aliquip ex ea commodo consequat. Duis aute irure dolor in reprehenderit in voluptate velit esse cillum dolore eu fugiat nulla pariatur.</p>
      <p class="body">Lorem ipsum dolor sit amet, consectetur adipisicing elit, sed do eiusmod tempor incididunt ut labore et dolore magna aliqua. Ut enim ad minim veniam, quis nostrud exercitation ullamco laboris nisi ut aliquip ex ea commodo consequat.</p>
      <p class="body">Excepteur sint occaecat cupidatat non proident, sunt in culpa qui officia deserunt mollit anim id est laborum. re et dolore magnam aliquam quaerat voluptatem.</p>
      <div class="closing">Regards</div>
      <div class="signature">Daniel Carter</div>
    </section>

    <svg class="footer-wave" width="580" height="820" viewBox="0 0 580 820" aria-hidden="true">
      <path d="M0,820 L0,812 C200,810 420,772 580,672 L580,820 Z" fill="var(--gold)"/>
      <path d="M40,802 C220,796 430,752 560,640 C440,744 230,794 40,805 Z" fill="var(--navy)"/>
    </svg>

    <address class="contact">
      <div class="contact-line">
        <svg width="9" height="9" viewBox="0 0 24 24"><path fill="var(--gold)" d="M6.6 10.8a15.1 15.1 0 0 0 6.6 6.6l2.2-2.2c.3-.3.7-.4 1-.2 1.1.4 2.3.6 3.6.6.6 0 1 .4 1 1V20c0 .6-.4 1-1 1A17 17 0 0 1 3 4c0-.6.4-1 1-1h3.5c.6 0 1 .4 1 1 0 1.3.2 2.5.6 3.6.1.3 0 .7-.2 1z"/></svg>
        <span>555-618-2450</span>
        <svg width="9" height="9" viewBox="0 0 24 24" style="margin-left:4px"><path fill="var(--gold)" d="M6 2h9l3 3v4H6zM3 10h18a1 1 0 0 1 1 1v7h-4v4H6v-4H2v-7a1 1 0 0 1 1-1zm5 7v3h8v-3z"/></svg>
        <span>800-394-8261</span>
      </div>
      <div class="contact-line">
        <svg width="9" height="11" viewBox="0 0 24 30"><path fill="var(--gold)" d="M12 0a10 10 0 0 0-10 10c0 7.5 10 20 10 20s10-12.5 10-20A10 10 0 0 0 12 0zm0 14a4 4 0 1 1 0-8 4 4 0 0 1 0 8z"/></svg>
        <span>4829 NW 58th Lane, Suite 310 Coral Bend, FL 33468</span>
      </div>
    </address>
  </main>
</body>
</html>
```